Business card New design- upscale

Looking for modern design business cards. Minimalist, mix of gloss and matte finishes. Texas based Contractor company doing Mechanical hvac and plumbing, focused on commercial and industrial manufacturing facilities. We don't hand too many out so high end materials or functionality...will be considered. Please see attached files for info needed on cards. *New plumbing license needs to be edited to say K82917. Www.valtrimgroup.com
P.s. Website will also be redesigned soon.

Target Market(s)

Facility managers for commercial buildings, mechanical engineers for industrial manufacturing facilities including pharmaceutical, semiconductor, food & beverage, etc

Contact Information for Business Card

See attached images

Requirements
Must have
• All Logo colors: purple, black and Gray. 1, 2 or 4 rounded corners. All content on existing business cards (see attached images).
Nice to have
• Matte and gloss print. Embossing, raised print, functionality.
Should not have
• Stock images, generic construction.

```html
<!DOCTYPE html>
<html lang="en">
<head>
<meta charset="utf-8">
<title>Valtrim Group – Business Card</title>
<link href="https://fonts.googleapis.com/css2?family=Montserrat:wght@500;600;700;800&display=swap" rel="stylesheet">
<style>
  :root {
    --purple: #3d2266;
    --purple-deep: #37205e;
    --purple-soft: #4f3080;
    --ink: #4a4a4a;
    --gray: #6b6b6b;
    --paper: #ffffff;
    --backdrop: #3a3638;
  }
  * { box-sizing: border-box; margin: 0; padding: 0; }
  html, body { width: 1200px; height: 881px; overflow: hidden; }
  body {
    background: var(--backdrop);
    font-family: "Montserrat", sans-serif;
    position: relative;
  }
  .card {
    position: absolute;
    width: 530px;
    height: 303px;
    border-radius: 22px;
    overflow: hidden;
    box-shadow: 0 10px 24px rgba(0,0,0,.35);
  }
  /* Front */
  .card-front {
    left: 40px; top: 289px;
    background: linear-gradient(100deg, var(--purple-soft) 0%, var(--purple) 35%, var(--purple-deep) 100%);
    display: flex; align-items: center; justify-content: center;
  }
  .front-brand {
    display: flex; align-items: center; gap: 16px;
    color: #5a3b8c;
    font-weight: 700;
    font-size: 46px;
    letter-spacing: 4px;
  }
  .brand-square { width: 26px; height: 26px; background: #5a3b8c; }

  /* Back */
  .card-back {
    left: 630px; top: 289px;
    background: var(--paper);
  }
  .accent-bar {
    position: absolute; left: 0; top: 148px;
    width: 10px; height: 58px; background: var(--purple);
  }
  .info-col {
    position: absolute; left: 34px; top: 30px; width: 270px;
  }
  .back-brand {
    display: flex; align-items: center; gap: 8px;
    color: var(--purple); font-weight: 700; font-size: 23px; letter-spacing: 2px;
  }
  .back-brand .brand-square { width: 16px; height: 16px; background: var(--purple); }
  .person-name {
    margin-top: 16px;
    color: var(--purple); font-weight: 800; font-size: 24px; letter-spacing: 2px;
  }
  .person-title {
    margin-top: 4px;
    color: var(--gray); font-weight: 700; font-size: 13.5px; line-height: 1.25;
  }
  .contact-list { list-style: none; margin-top: 10px; }
  .contact-list li {
    display: flex; align-items: center; gap: 7px;
    color: var(--gray); font-weight: 600; font-size: 13px; line-height: 1.45;
  }
  .contact-list svg { width: 11px; height: 11px; flex: none; }
  .tagline {
    margin-top: 12px;
    color: var(--purple); font-weight: 700; font-size: 13.5px; line-height: 1.3;
  }
  .license-col {
    position: absolute; right: 42px; top: 26px; width: 200px;
    text-align: right;
    color: var(--ink); font-weight: 600; font-size: 10.5px; line-height: 1.33;
  }
  .license-divider {
    position: absolute; right: 28px; top: 28px;
    width: 1.5px; height: 208px; background: var(--purple);
  }
  .license-url {
    position: absolute; right: 34px; bottom: 26px;
    color: var(--purple); font-weight: 700; font-size: 13px;
  }
</style>
</head>
<body>

  <section class="card card-front" aria-label="Card front">
    <div class="front-brand"><span class="brand-square"></span>VALTRIM GROUP</div>
  </section>

  <section class="card card-back" aria-label="Card back">
    <div class="accent-bar"></div>

    <div class="info-col">
      <div class="back-brand"><span class="brand-square"></span>VALTRIM GROUP</div>
      <h1 class="person-name">DALE MORROW</h1>
      <p class="person-title">Lead Estimator/Sr.<br>Project Manager</p>
      <ul class="contact-list">
        <li>
          <svg viewBox="0 0 12 12" fill="none" stroke="#555" stroke-width="1.3"><rect x="3" y="1" width="6" height="10" rx="1"/></svg>
          (520) 555-0186
        </li>
        <li>
          <svg viewBox="0 0 12 12" fill="#555"><path d="M3 1l2 2-1 1.5c.7 1.5 1.8 2.6 3.5 3.5L9 7l2 2-1.5 2C5 10.5 1.5 7 1 2.5z"/></svg>
          (817) 555-0142
        </li>
        <li>
          <svg viewBox="0 0 12 12" fill="none" stroke="#555" stroke-width="1.2"><rect x="1" y="2.5" width="10" height="7"/><path d="M1 2.5l5 4 5-4"/></svg>
          dmorrow@valtrimgroup.com
        </li>
        <li>
          <svg viewBox="0 0 12 12" fill="none" stroke="#555" stroke-width="1"><circle cx="6" cy="6" r="5"/><ellipse cx="6" cy="6" rx="2.2" ry="5"/><path d="M1 6h10"/></svg>
          www.valtrimgroup.com
        </li>
      </ul>
      <p class="tagline">Commercial &amp; Industrial Contractors<br>Mechanical &amp; Plumbing Services</p>
    </div>

    <div class="license-divider"></div>
    <div class="license-col">
      K82917 Regulated by<br>
      the State Plumbing<br>
      Examiners Board,<br>
      P.O. Box 1040,<br>
      Austin, TX. 78700;<br>
      1-800-555-0110,<br>
      512-555-0120 /<br>
      TACLA51730C<br>
      Regulated by the State<br>
      Licensing &amp; Regulation<br>
      Office, P.O. Box 1260,<br>
      Austin, TX. 78701;<br>
      1-800-555-0130,<br>
      512-555-0140
    </div>
    <div class="license-url">www.txlicenseboard.org</div>
  </section>

</body>
</html>
```